Web design needed for business broker

I need a design for a home page for a website I am coding. We are building a new site for an existing company and their existing site is www.qdventures.com.au

For the office contact details will be

(02) 5184 6297
hello@qdventures.com.au

Location – Australia Wide

Logos are attached. This will be for the brokerage side of things. I also want to set up one of the pages which will almost have its own landing page style setup for consulting. The Logo will be slightly different (Attached as colour logo with Black Background). The consulting will operate Under Quartz Dale Ventures, however we are changing to QD Ventures for the Brokerage Arm.

The home page should have the following:

Small amount of Intro Text (Can use something from the current website for now)
Latest Listings
Recently Sold
“The Selling Process”
Also want something (either a pop up or major focus on front page to be about getting a free business appraisal).

```html
<!DOCTYPE html>
<html lang="en">
<head>
<meta charset="utf-8">
<title>QD Ventures – Business Broker Specialists</title>
<link rel="stylesheet" href="https://fonts.googleapis.com/css2?family=Playfair+Display:wght@500;600;700&family=Poppins:wght@400;500;600&display=swap">
<style>
:root{
  --gold:#b8862e;
  --gold-light:#d6a64a;
  --yellow:#f4c12e;
  --brown:#8a5a1f;
  --ink:#111;
  --text:#555;
  --muted:#777;
  --grey-bg:#f0f0f0;
  --line:#e6e6e6;
  --footer:#000;
}
*{box-sizing:border-box;margin:0;padding:0}
html,body{width:1200px;height:4963px;overflow:hidden}
body{font-family:"Poppins",sans-serif;color:var(--text);background:#fff;position:relative}
a{color:inherit;text-decoration:none}
.abs{position:absolute}
section,header,footer{position:absolute;left:0;width:1200px}
.section-title{position:absolute;left:0;width:1200px;text-align:center;font-family:"Playfair Display",serif;font-weight:600;font-size:33px;color:var(--ink);display:flex;justify-content:center;align-items:center;gap:8px}
.section-title::before,.section-title::after{content:"";width:36px;height:2px;background:var(--gold-light)}
.section-sub{position:absolute;left:0;width:1200px;text-align:center;font-size:12px;color:var(--text)}
.btn-yellow{position:absolute;background:var(--yellow);color:var(--ink);border-radius:20px;font-size:12px;display:flex;align-items:center;justify-content:center}
.read-more{font-size:11px;color:var(--ink);display:flex;align-items:center;gap:6px}
.read-more::after{content:"→";color:var(--gold);font-size:11px}

/* hero */
.hero{top:0;height:612px;background:linear-gradient(105deg,#3a3530 0%,#5b544c 45%,#7a7168 70%,#4a443e 100%)}
.hero-photo{position:absolute;inset:0;background:radial-gradient(ellipse at 75% 55%,rgba(160,150,140,.45),transparent 60%),linear-gradient(180deg,rgba(0,0,0,.25),rgba(0,0,0,.4))}
.brand{position:absolute;left:140px;top:58px;display:flex;align-items:center;gap:8px}
.brand-dot{width:12px;height:12px;border-radius:50%;background:var(--gold-light)}
.brand-name{font-size:14px;font-weight:500;color:var(--gold-light)}
.nav{position:absolute;top:48px;left:412px;display:flex;align-items:center;height:43px}
.nav a{font-size:13px;color:#fff;margin-right:22px}
.nav a.active{color:var(--gold-light);border-bottom:1px solid var(--gold-light)}
.nav .cta{margin-left:2px;width:141px;height:43px;background:var(--brown);border:1px solid var(--gold-light);display:flex;align-items:center;justify-content:center;color:#fff;font-size:12px}
.hero h1{position:absolute;left:138px;top:244px;font-size:32px;font-weight:600;color:#fff}
.hero p{position:absolute;left:142px;top:302px;width:560px;font-size:15px;line-height:28px;color:#f2f2f2}
.hero .btn-contact{position:absolute;left:143px;top:439px;width:125px;height:42px;background:var(--brown);border:1px solid var(--gold-light);color:#fff;font-size:12px;display:flex;align-items:center;justify-content:center}
.video-play{position:absolute;left:1108px;top:178px;width:28px;display:flex;flex-direction:column;align-items:center;color:#fff;font-size:16px;font-weight:500;line-height:35px}
.play-btn{width:44px;height:44px;border-radius:50%;border:2px solid #fff;display:flex;align-items:center;justify-content:center;margin:4px 0}
.scroll-mouse{position:absolute;left:565px;top:577px;width:70px;height:70px;border-radius:50%;background:#fff;box-shadow:0 2px 8px rgba(0,0,0,.15);display:flex;align-items:center;justify-content:center;z-index:3}

/* about */
.about{top:612px;height:870px}
.about-img-a{position:absolute;left:140px;top:130px;width:224px;height:318px;background:linear-gradient(135deg,#6c5040,#c7b5a5 55%,#3e3a38)}
.about-img-b{position:absolute;left:364px;top:89px;width:218px;height:319px;background:linear-gradient(140deg,#d7dde2,#5e6670 55%,#2c2f36)}
.about h2{position:absolute;left:618px;top:124px;font-family:"Playfair Display",serif;font-weight:600;font-size:33px;color:var(--ink);display:flex;align-items:center;gap:6px}
.about h2::after{content:"";width:36px;height:2px;background:var(--gold-light)}
.about h4{position:absolute;left:618px;top:174px;font-size:12.5px;font-weight:500;color:var(--ink)}
.about p{position:absolute;left:618px;top:200px;width:440px;font-size:11.3px;line-height:21.6px;color:var(--text)}
.about .btn-yellow{left:618px;top:376px;width:130px;height:32px}

/* services */
.services-title{top:1134px}
.service-card{position:absolute;top:1194px;width:293px;height:206px;border:1px solid var(--line);background:#fff;padding:26px 22px}
.service-head{display:flex;align-items:center;gap:8px;font-size:15px;color:var(--ink);font-weight:500}
.service-card p{margin-top:18px;font-size:11px;line-height:21.5px;color:var(--text)}
.service-card .read-more{margin-top:10px}

/* featured */
.featured{top:1487px;height:630px;background:var(--grey-bg)}
.slider-prev,.slider-next{position:absolute;width:34px;height:34px;border-radius:50%;display:flex;align-items:center;justify-content:center;font-size:15px}
.slider-prev{border:1px solid #333;color:#333;background:#fff}
.slider-next{background:var(--yellow);color:#333}
.listing{position:absolute;width:276px;background:#fff;padding:6px}
.listing-img{height:200px}
.listing-body{padding:16px 12px 0}
.status{font-size:14px;color:var(--gold);text-decoration:underline;font-weight:500}
.price{font-size:15px;color:var(--ink);margin-top:6px}
.listing-title{font-size:11.5px;color:var(--ink);font-weight:500;margin-top:4px;line-height:18px}
.loc{font-size:10px;color:var(--muted);margin-top:4px;display:flex;gap:5px;line-height:13px}
.loc::before{content:"";flex:none;width:8px;height:10px;margin-top:1px;border-radius:50% 50% 50% 0;transform:rotate(-45deg);background:var(--gold-light)}

/* selling process */
.process{top:2117px;height:811px}
.proc-label{position:absolute;font-size:11px;line-height:22px;color:var(--text)}
.proc-label strong{display:block;font-size:15px;font-weight:500;color:var(--ink);margin-bottom:4px}
.offer-box{position:absolute;left:451px;top:550px;width:294px;height:112px;background:#fff;border-bottom:2px solid var(--gold-light);box-shadow:0 2px 10px rgba(0,0,0,.05);text-align:center;padding-top:12px;font-size:11px;line-height:22px}
.offer-box strong{display:block;font-size:15px;font-weight:500;color:var(--ink);margin-bottom:4px}

/* recently sold */
.sold{top:2928px;height:724px;background:var(--grey-bg)}
.sold-badge{position:absolute;left:6px;top:6px;width:44px;height:44px;background:var(--yellow);font-size:11px;color:var(--ink);display:flex;align-items:center;justify-content:center}
.sold .listing-title{font-size:15px;margin-top:0}
.sold .desc{font-size:11px;color:var(--ink);margin-top:8px;line-height:19.5px}

/* news */
.news{top:3652px;height:745px}
.news-img{position:absolute}
.news-text{position:absolute;padding:18px 20px;background:#fff}
.news-date{font-size:11px;color:var(--gold)}
.news-title{font-size:15px;color:var(--ink);font-weight:500;margin-top:2px;line-height:22px}
.news-by{font-size:10px;color:var(--muted);margin-top:8px;display:flex;gap:6px;align-items:center}
.news-by::before{content:"";width:9px;height:9px;border-radius:50%;background:var(--gold-light)}
.news-by span{color:var(--gold)}
.news-excerpt{font-size:11px;line-height:20px;color:var(--text);margin-top:12px}
.news .read-more{margin-top:18px}
.boxed{border:1px solid var(--line)}

/* footer */
footer{top:4397px;height:566px;background:var(--footer);color:#fff}
.footer-brand{position:absolute;left:0;width:1200px;top:100px;display:flex;justify-content:center;align-items:center;gap:12px}
.footer-brand .name{font-family:"Poppins",sans-serif;font-weight:500;font-size:28px;color:var(--gold-light)}
.f-head{position:absolute;top:218px;font-family:"Playfair Display",serif;font-size:15px;display:flex;align-items:center;gap:8px}
.f-head::after{content:"";width:34px;height:2px;background:var(--gold-light)}
.f-text{position:absolute;left:140px;top:256px;width:310px;font-size:11px;line-height:22px}
.f-input{position:absolute;left:140px;top:335px;width:309px;height:34px;border:1px solid #fff;border-radius:18px;font-size:11px;padding-left:14px;display:flex;align-items:center}
.f-sub{position:absolute;left:140px;top:385px;width:142px;height:33px;background:var(--yellow);color:var(--ink);border-radius:18px;font-size:11px;display:flex;align-items:center;justify-content:center;gap:7px}
.f-col{position:absolute;top:260px;font-size:11px;line-height:20.5px;display:flex;flex-direction:column}
.f-contact{position:absolute;top:465px;display:flex;align-items:center;gap:12px;font-size:11px;line-height:18px}
.f-icon{width:34px;height:34px;border-radius:50%;background:#fff;display:flex;align-items:center;justify-content:center}
.f-copy{position:absolute;left:140px;top:536px;font-size:10px}
.f-social{position:absolute;left:924px;top:529px;display:flex;gap:8px}
.f-social span{width:26px;height:26px;border-radius:50%;background:#555}
</style>
</head>
<body>

<header class="hero">
  <div class="hero-photo" role="img" aria-label="Photo of business people reviewing documents and charts at a desk"></div>
  <div class="brand"><span class="brand-dot"></span><span class="brand-name">Quartz Dale Ventures</span></div>
  <nav class="nav">
    <a href="#" class="active">Home</a><a href="#">Buy</a><a href="#">Sell</a><a href="#">Services</a><a href="#">About</a><a href="#">Join Our Team</a><a href="#">Contact</a>
    <a href="#" class="cta">Free Appraisal</a>
  </nav>
  <h1>How much is your Business worth?</h1>
  <p>Lorem ipsum dolor sit amet, consectetur adipiscing elit, sed do eiusmod tempor incididunt ut labore et dolore magna aliqua. Quis ipsum suspendisse ultrices gravida. Risus commodo viverra maecenas accumsan lacus vel facilisis.</p>
  <a href="#" class="btn-contact">Contact Us</a>
  <div class="video-play">
    <span>V</span><span>I</span><span>D</span><span>E</span><span>O</span>
    <span class="play-btn"><svg width="14" height="16" viewBox="0 0 14 16"><path d="M2 1l11 7-11 7z" fill="#fff"/></svg></span>
    <span>P</span><span>L</span><span>A</span><span>Y</span>
  </div>
</header>
<div class="scroll-mouse"><svg width="22" height="34" viewBox="0 0 22 34"><rect x="2" y="2" width="18" height="30" rx="9" fill="none" stroke="#b8862e" stroke-width="2"/><line x1="11" y1="8" x2="11" y2="13" stroke="#b8862e" stroke-width="2"/></svg></div>

<section class="about">
  <div class="about-img-a" role="img" aria-label="Photo of two businesswomen in a meeting"></div>
  <div class="about-img-b" role="img" aria-label="Photo of a businessman discussing at a laptop"></div>
  <h2>About Us</h2>
  <h4>We are Quartz Dale Ventures.</h4>
  <p>Our business brokerage services are designed to help you buy or sell a business quickly, efficiently, and at the best possible price. We understand that selling or buying a business can be overwhelming, which is why we work closely with our clients to ensure a smooth and successful transaction. Our team of experts has years of experience in business sales and acquisitions, providing you with the knowledge and support you need to make informed decisions.</p>
  <a href="#" class="btn-yellow">Read More</a>
</section>

<h2 class="section-title services-title">Our Services</h2>
<div class="service-card" style="left:140px">
  <div class="service-head"><svg width="40" height="40" viewBox="0 0 40 40" fill="none" stroke="#222" stroke-width="1.6"><rect x="8" y="16" width="24" height="18" rx="2"/><path d="M15 16v-4h10v4"/><circle cx="30" cy="10" r="5" stroke="#b8862e"/></svg>Business Sales</div>
  <p>We are specialist brokers working with you to position your business to ensure it has the best possible results when selling...</p>
  <a class="read-more" href="#">Find Out More</a>
</div>
<div class="service-card" style="left:453px">
  <div class="service-head"><svg width="40" height="40" viewBox="0 0 40 40" fill="none" stroke="#222" stroke-width="1.6"><rect x="6" y="10" width="10" height="24"/><rect x="24" y="10" width="10" height="24"/><path d="M16 20h8" stroke="#b8862e"/></svg>Mergers and Acquisitions</div>
  <p>If you're considering the sale of your larger business, Quartz Dale Ventures is here to amplify your potential...</p>
  <a class="read-more" href="#">Find Out More</a>
</div>
<div class="service-card" style="left:765px">
  <div class="service-head"><svg width="40" height="40" viewBox="0 0 40 40" fill="none" stroke="#222" stroke-width="1.6"><rect x="6" y="8" width="28" height="18" rx="2"/><circle cx="14" cy="31" r="3"/><circle cx="26" cy="31" r="3"/><path d="M12 18l6-5 5 4 6-5" stroke="#b8862e"/></svg>Business Consulting</div>
  <p>With our dedicated team of business consultants you are working with people who have experience growing...</p>
  <a class="read-more" href="#">Find Out More</a>
</div>

<section class="featured">
  <h2 class="section-title" style="top:96px">Featured Businesses</h2>
  <span class="slider-prev" style="left:86px;top:306px">←</span>
  <span class="slider-next" style="left:1081px;top:306px">→</span>
  <article class="listing" style="left:145px;top:141px;height:405px">
    <div class="listing-img" role="img" aria-label="Photo of a chocolate shop interior with shelves of gifts" style="background:linear-gradient(160deg,#5b3b2a,#a77b55 50%,#e0d0bf)"></div>
    <div class="listing-body">
      <div class="status">FOR SALE</div>
      <div class="price">$8,00,000</div>
      <div class="listing-title">Cocoa Lane &amp; The Harbour</div>
      <div class="loc">Cocoa Lane &amp; The Harbour Confectionery School</div>
      <a class="read-more" href="#" style="margin-top:24px">Read More</a>
    </div>
  </article>
  <article class="listing" style="left:462px;top:141px;height:405px">
    <div class="listing-img" role="img" aria-label="Photo of a crowd at an event under purple stage lights" style="background:linear-gradient(170deg,#3a4bc0,#6a3fa5 45%,#1b1530)"></div>
    <div class="listing-body">
      <div class="status">FOR SALE</div>
      <div class="price">Offers Over $1,000,000</div>
      <div class="listing-title">Events Management &amp; Styling</div>
      <div class="loc">Events Management &amp; Styling Company</div>
      <a class="read-more" href="#" style="margin-top:37px">Read More</a>
    </div>
  </article>
  <article class="listing" style="left:780px;top:141px;height:405px">
    <div class="listing-img" role="img" aria-label="Photo of vacuuming a bright living room" style="background:linear-gradient(160deg,#d9c9a8,#efebe4 55%,#b9b4ac)"></div>
    <div class="listing-body">
      <div class="status">UNDER CONTRACT</div>
      <div class="price">$450,000</div>
      <div class="listing-title">UNDER OFFER - Domestic</div>
      <div class="loc">Willow Domestic Services Pty Limited</div>
      <a class="read-more" href="#" style="margin-top:37px">Read More</a>
    </div>
  </article>
</section>

<section class="process">
  <h2 class="section-title" style="top:80px">Selling Process</h2>
  <svg class="abs" style="left:0;top:0" width="1200" height="811" viewBox="0 0 1200 811" fill="none">
    <g stroke="#eee" stroke-width="1.5">
      <path d="M330 230 a300 300 0 0 1 210 -120"/>
      <path d="M660 110 a300 300 0 0 1 210 120"/>
      <path d="M380 360 a230 230 0 0 1 -20 -90"/>
      <path d="M840 270 a230 230 0 0 1 -20 90"/>
      <path d="M440 420 a200 200 0 0 0 100 60"/>
      <path d="M660 480 a200 200 0 0 0 100 -60"/>
    </g>
    <circle cx="612" cy="194" r="68" fill="#fff" stroke="#eee" stroke-width="2"/>
    <text x="612" y="199" text-anchor="middle" font-family="Poppins, sans-serif" font-weight="500" font-size="15" fill="#b8862e">QD Ventures</text>
    <path d="M496 200 a116 116 0 0 0 232 0" stroke="#d6a64a" stroke-width="3"/>
    <g fill="#d6a64a"><circle cx="514" cy="262" r="3"/><circle cx="562" cy="300" r="3"/><circle cx="662" cy="300" r="3"/><circle cx="710" cy="262" r="3"/></g>
    <g stroke="#333" stroke-width="1.6">
      <rect x="382" y="254" width="34" height="22" rx="2"/><path d="M388 246l22-14m-6 0h6v6" stroke="#b8862e"/>
      <rect x="456" y="364" width="30" height="38" rx="2"/><path d="M463 374h16M463 382h16M463 390h16"/>
      <rect x="594" y="407" width="36" height="30" rx="2"/><path d="M594 411l18 12 18-12"/><text x="612" y="403" text-anchor="middle" font-size="8" font-family="Poppins, sans-serif" fill="#333" stroke="none">OFFER</text>
      <path d="M730 358h42v20h-42z"/><path d="M741 358l10-10 10 10"/><text x="751" y="372" text-anchor="middle" font-size="9" font-family="Poppins, sans-serif" fill="#333" stroke="none">SOLD</text>
      <path d="M800 268l12-10 10 8 10-8 12 10-18 16z"/><circle cx="820" cy="250" r="6" stroke="#b8862e"/>
    </g>
    <g stroke="#555" stroke-width="1">
      <path d="M316 300v82h-10"/>
      <path d="M397 458v126h-10"/>
      <path d="M612 520v26"/><circle cx="612" cy="548" r="2" fill="#d6a64a" stroke="none"/>
      <path d="M828 458v126h10"/>
      <path d="M900 300v82h10"/>
    </g>
  </svg>
  <div class="proc-label" style="left:142px;top:309px;width:160px"><strong>Appraisal</strong>We specialise in the marketing, listing and selling of your business.</div>
  <div class="proc-label" style="left:223px;top:468px;width:160px"><strong>Prepare</strong>Gather all documentation and prepare the documentation needed during due diligence.</div>
  <div class="offer-box"><strong>Offer</strong>Expert negotiations to<br>ensure you have the best<br>results.</div>
  <div class="proc-label" style="left:857px;top:468px;width:150px"><strong>Sold</strong>Due diligence and finalisation of the sales process.</div>
  <div class="proc-label" style="left:930px;top:309px;width:135px"><strong>Deal Closed</strong>Lorem ipsum is simply dummy text of the printing &amp; typesetting industry.</div>
  <a href="#" class="btn-yellow" style="left:535px;top:693px;width:130px;height:33px">Get Started</a>
</section>

<section class="sold">
  <h2 class="section-title" style="top:80px">Recently Sold</h2>
  <p class="section-sub" style="top:140px">Browse from a list of recently sold businesses.</p>
  <span class="slider-prev" style="left:86px;top:364px">←</span>
  <span class="slider-next" style="left:1081px;top:364px">→</span>
  <article class="listing" style="left:145px;top:179px;height:397px">
    <div class="listing-img" role="img" aria-label="Photo of an outdoor cafe with umbrellas and timber seating" style="background:linear-gradient(180deg,#4a6fa8,#a9b7c6 45%,#a5683a)"></div>
    <span class="sold-badge">Sold</span>
    <div class="listing-body">
      <div class="listing-title">Contact For Price</div>
      <div class="desc">SOLD - Maple Cup Coffee Shop</div>
      <div class="loc">Macquarie ACT</div>
      <a class="read-more" href="#" style="margin-top:62px">Read More</a>
    </div>
  </article>
  <article class="listing" style="left:462px;top:179px;height:397px">
    <div class="listing-img" role="img" aria-label="Photo of a burger being held in a dark setting" style="background:linear-gradient(160deg,#2a2420,#8a6a40 55%,#1f1a17)"></div>
    <span class="sold-badge">Sold</span>
    <div class="listing-body">
      <div class="listing-title">Contact For Price</div>
      <div class="desc">SOLD - Popular Burger Joint in Adelaide with additional Passive Income Opportunity</div>
      <div class="loc">Prospect SA</div>
      <a class="read-more" href="#" style="margin-top:22px">Read More</a>
    </div>
  </article>
  <article class="listing" style="left:780px;top:179px;height:397px">
    <div class="listing-img" role="img" aria-label="Photo of a dim bar and cafe interior with leather seating" style="background:linear-gradient(160deg,#6b6660,#2e2a27 60%,#15120f)"></div>
    <span class="sold-badge">Sold</span>
    <div class="listing-body">
      <div class="listing-title">Contact For Price</div>
      <div class="desc">SOLD - Bar and Cafe overlooking the Harbour in Ulladulla</div>
      <div class="loc">Ulladulla NSW</div>
      <a class="read-more" href="#" style="margin-top:42px">Read More</a>
    </div>
  </article>
  <a href="#" class="btn-yellow" style="left:465px;top:624px;width:270px;height:34px">View More View More Sold Businesses</a>
</section>

<section class="news">
  <h2 class="section-title" style="top:80px">Latest News &amp; Tips</h2>
  <p class="section-sub" style="top:140px">Read the latest news and information from the world of business.</p>
  <div class="news-img" role="img" aria-label="Photo of two businessmen reviewing papers at a desk" style="left:140px;top:177px;width:264px;height:225px;background:linear-gradient(150deg,#c9d3dc,#556270 55%,#2d3440)"></div>
  <div class="news-text" style="left:404px;top:177px;width:351px;height:225px">
    <div class="news-date">Mar 06, 2024</div>
    <div class="news-title">Trending Industries</div>
    <div class="news-by">Posted By <span>Mara Holloway</span></div>
    <div class="news-excerpt">The latest data released from the National Statistics Office (NSO)shows strong growth across most services style businesses including a HUGE growth...</div>
    <a class="read-more" href="#">Read More</a>
  </div>
  <div class="news-text boxed" style="left:140px;top:425px;width:347px;height:223px">
    <div class="news-date">Feb 28, 2024</div>
    <div class="news-title">Buying a Business for Beginners: What You Need to Know</div>
    <div class="news-by">Posted By <span>Mara Holloway</span></div>
    <div class="news-excerpt">Are you considering taking the leap into business ownership by purchasing an existing enterprise?...</div>
    <a class="read-more" href="#">Read More</a>
  </div>
  <div class="news-img" role="img" aria-label="Photo of a woman shrugging in front of a bookshelf" style="left:493px;top:425px;width:262px;height:223px;background:linear-gradient(150deg,#4b3d33,#9a8b7e 50%,#d9d4ce)"></div>
  <div class="news-img" role="img" aria-label="Illustration of a hand holding a money bag with a dollar sign" style="left:778px;top:177px;width:279px;height:225px;background:linear-gradient(160deg,#56a5a2,#3f8f8c)"></div>
  <div class="news-text boxed" style="left:778px;top:402px;width:279px;height:246px">
    <div class="news-date">Feb 28, 2024</div>
    <div class="news-title">Exploring Vendor Finance: Pros &amp; Cons for Selling Your Business</div>
    <div class="news-by">Posted By <span>Mara Holloway</span></div>
    <div class="news-excerpt">Selling a business is a significant decision, one that often comes ...</div>
    <a class="read-more" href="#">Read More</a>
  </div>
</section>

<footer>
  <div class="footer-brand"><span class="name">QD Ventures</span></div>
  <div class="f-head" style="left:140px">Get The Latest On Prices</div>
  <p class="f-text">Subscribe to get the latest insider tips, market updates and access to the hottest deals as they come on the market.</p>
  <div class="f-input">Enter Your Email Address</div>
  <a href="#" class="f-sub"><svg width="14" height="10" viewBox="0 0 14 10"><rect x=".5" y=".5" width="13" height="9" fill="none" stroke="#111"/><path d="M.5 .5l6.5 5 6.5-5" fill="none" stroke="#111"/></svg>Subscribe Now</a>
  <div class="f-head" style="left:505px">Quick Links</div>
  <div class="f-col" style="left:505px"><a>Browse All Businesses</a><a>Request Appraisal</a><a>About</a><a>Services</a></div>
  <div class="f-col" style="left:680px"><a>Contact</a><a>Quartz Dale Ventures</a><a>Market Appraisal</a><a>Join Our Team</a></div>
  <div class="f-col" style="left:878px"><a>Recently Sold</a><a>Why Sell With Us</a><a>News</a><a>Free Appraisal</a></div>
  <div class="f-col" style="left:1025px"><a>Home</a><a>Buy</a><a>Sell</a></div>
  <div class="f-contact" style="left:140px"><span class="f-icon"><svg width="16" height="12" viewBox="0 0 16 12"><rect x=".5" y=".5" width="15" height="11" fill="none" stroke="#111"/><path d="M.5 .5l7.5 6 7.5-6" fill="none" stroke="#111"/></svg></span><span>Email<br>hello@qdventures.com.au</span></div>
  <div class="f-contact" style="left:561px"><span class="f-icon"><svg width="12" height="16" viewBox="0 0 12 16"><path d="M6 15s5-6 5-9A5 5 0 0 0 1 6c0 3 5 9 5 9z" fill="#111"/><circle cx="6" cy="6" r="2" fill="#fff"/></svg></span><span>14/27 Wattle Rd,<br>Fyshwick ACT 2609</span></div>
  <div class="f-contact" style="left:934px"><span class="f-icon"><svg width="14" height="14" viewBox="0 0 14 14"><path d="M3 1l2 3-1.5 1.5a8 8 0 0 0 5 5L10 9l3 2-1.5 2.5C6 13 1 8 .5 2.5z" fill="#111"/></svg></span><span>Phone<br>(02) 5184 6297</span></div>
  <p class="f-copy">© 2023 - 2024 | Quartz Dale Ventures , All Rights Reserved | Privacy Policy. Powered by Kestrel Digital</p>
  <div class="f-social"><span></span><span></span><span></span><span></span></div>
</footer>

</body>
</html>
```